KitVarro.com FACELIFT design for the online store

A) GENERAL
We need a small FACELIFT design with a short styleguide for our online store http://KitVarro.com (online store for sport goods; the store is just now in responsive design; actually only in German). The store is the first online store worldwide with 3d images for all products.
B) Designers: PLEASE NOTE:
- We don't want change functionality!
- We only want a small facelift.
- We don't need a fully coded website.
C) We only need for the responsive design views:
1. the home page design (one page)
http://www.kitvarro.com/de/
2. the category listing design (one page)
http://www.kitvarro.com/de/alle/running.html
3. the product detail page (one page)
http://www.kitvarro.com/de/pembrik-tz-flo-3d-hvx-herren-traillaufschuhe-drelon-wex.html
4. the cms page (textonly !!!)
http://www.kitvarro.com/de/versand-und-lieferung
5. the Mega drop down
D) We intend to change/use:
- maybe to use a background image in the start page, and each category
- change the header
- change the font sizes for the titles (maybe in capital letters)
- change the mega drop down
Europe
Store
4 page

```html
<!DOCTYPE html>
<html lang="en">
<head>
<meta charset="utf-8">
<title>Outdoor Clothing – KitVarro.com</title>
<link rel="stylesheet" href="https://fonts.googleapis.com/css2?family=Roboto:wght@400&display=swap">
<style>
  :root {
    --bg: #ffffff;
    --header-bg: #f4f4f4;
    --title: #777777;
    --text: #111111;
    --icon: #222222;
    --divider: #e3e3e3;
  }
  * { box-sizing: border-box; margin: 0; padding: 0; }
  html, body {
    width: 1200px;
    height: 3493px;
    overflow: hidden;
    background: var(--bg);
    font-family: "Roboto", sans-serif;
  }
  .screen {
    position: relative;
    width: 1200px;
    height: 3493px;
    background: var(--bg);
  }
  .app-header {
    position: relative;
    height: 105px;
    background: var(--header-bg);
    display: flex;
    align-items: center;
    justify-content: center;
  }
  .back-button {
    position: absolute;
    left: 74px;
    top: 36px;
    width: 34px;
    height: 38px;
  }
  .page-title {
    font-size: 34px;
    font-weight: 400;
    letter-spacing: 1px;
    color: var(--title);
    margin-left: -14px;
  }
  .category-list {
    list-style: none;
    margin-top: 45px;
  }
  .category-item {
    position: relative;
    height: 76.1px;
    border-bottom: 2px solid var(--divider);
    display: flex;
    align-items: center;
    padding-left: 87px;
  }
  .category-name {
    font-size: 33px;
    letter-spacing: 0.8px;
    color: var(--text);
    white-space: nowrap;
  }
  .chevron {
    position: absolute;
    left: 571px;
    top: 50%;
    width: 20px;
    height: 26px;
    transform: translateY(-50%);
  }
</style>
</head>
<body>
  <main class="screen">
    <header class="app-header">
      <svg class="back-button" viewBox="0 0 34 38" aria-label="Back">
        <polyline points="26,3 9,19 26,35" fill="none" stroke="var(--title)" stroke-width="5" stroke-linecap="round" stroke-linejoin="round"/>
      </svg>
      <h1 class="page-title">Outdoor Clothing</h1>
    </header>
    <ul class="category-list">
      <li class="category-item"><span class="category-name">Jackets</span><svg class="chevron" viewBox="0 0 20 26"><polyline points="5,3 15,13 5,23" fill="none" stroke="var(--icon)" stroke-width="3.5"/></svg></li>
      <li class="category-item"><span class="category-name">Sweater</span><svg class="chevron" viewBox="0 0 20 26"><polyline points="5,3 15,13 5,23" fill="none" stroke="var(--icon)" stroke-width="3.5"/></svg></li>
      <li class="category-item"><span class="category-name">Shirts and Shirts</span><svg class="chevron" viewBox="0 0 20 26"><polyline points="5,3 15,13 5,23" fill="none" stroke="var(--icon)" stroke-width="3.5"/></svg></li>
      <li class="category-item"><span class="category-name">Functional clothing</span><svg class="chevron" viewBox="0 0 20 26"><polyline points="5,3 15,13 5,23" fill="none" stroke="var(--icon)" stroke-width="3.5"/></svg></li>
      <li class="category-item"><span class="category-name">Pants</span><svg class="chevron" viewBox="0 0 20 26"><polyline points="5,3 15,13 5,23" fill="none" stroke="var(--icon)" stroke-width="3.5"/></svg></li>
      <li class="category-item"><span class="category-name">Gloves</span><svg class="chevron" viewBox="0 0 20 26"><polyline points="5,3 15,13 5,23" fill="none" stroke="var(--icon)" stroke-width="3.5"/></svg></li>
      <li class="category-item"><span class="category-name">Socks</span><svg class="chevron" viewBox="0 0 20 26"><polyline points="5,3 15,13 5,23" fill="none" stroke="var(--icon)" stroke-width="3.5"/></svg></li>
      <li class="category-item"><span class="category-name">Rainwear</span><svg class="chevron" viewBox="0 0 20 26"><polyline points="5,3 15,13 5,23" fill="none" stroke="var(--icon)" stroke-width="3.5"/></svg></li>
      <li class="category-item"><span class="category-name">Hats &amp; Headbands</span><svg class="chevron" viewBox="0 0 20 26"><polyline points="5,3 15,13 5,23" fill="none" stroke="var(--icon)" stroke-width="3.5"/></svg></li>
    </ul>
  </main>
</body>
</html>
```